BHAG Poster

We like creativity and visual boxes and shapes not just bullet points. We think we want it to be landscape view. Here are some of the parameters:

BHAG:
Become one of the most admired construction companies in the markets we serve within the next 10 years

3 – 5 year goals:
1. Generate 35m in revenue by 2020
2. Have a 50/50 mix of Public-Private job mix
3. Maintain 15% annual growth

1 year goals:
1. $24M in revenue with better margins
2. 14% gross margin on year
3. Business development begins to pay off
4. Continue recruiting great & talented people

Dynamic Quarter Goal:
(Leave this area blank so we can fill it in each quarter please)

Industry/Entity Type

Landscape

Colors
0355a3

Requirements
Must have
• SHAPES OR BOXES FOR VISUAL EFFECT. We don't want it to just be words on a page. Must be creative. Must have our logo somewhere on the poster. Our cmyk blue color is 100-80-0-22. Poster can have different colors, but it just needs to have some of our blue in it.
Should not have
• no bullet points

```html
<!DOCTYPE html>
<html lang="en">
<head>
<meta charset="utf-8">
<title>Harlow Construction – BHAG Poster</title>
<link href="https://fonts.googleapis.com/css2?family=Lato:wght@400;700;900&family=Questrial&display=swap" rel="stylesheet">
<style>
  :root {
    --brand-blue: #0355a3;
    --deep-blue: #123a8a;
    --navy: #0c2a6b;
    --slate: #4a4c50;
    --charcoal: #3d3f42;
    --ink: #1e1e22;
    --paper: #f7f8fa;
    --silver-light: #f2f2f2;
    --silver-dark: #b9bbbe;
    --rule: #8a8c90;
  }
  * { box-sizing: border-box; margin: 0; padding: 0; }
  html, body { width: 1200px; height: 944px; overflow: hidden; background: #e9e9e9; }
  .poster {
    position: relative; width: 1200px; height: 944px; overflow: hidden;
    background: linear-gradient(180deg, #ffffff 0%, var(--paper) 100%);
    font-family: "Lato", sans-serif; color: var(--ink);
  }
  .hero { position: absolute; inset: 0 0 auto 0; height: 320px; }
  .brand-panel {
    position: absolute; left: 40px; top: 0; width: 350px; height: 280px;
    background: linear-gradient(160deg, var(--silver-light) 0%, #dcdde0 55%, var(--silver-dark) 100%);
    box-shadow: 4px 6px 14px rgba(0,0,0,.35);
    border-bottom-right-radius: 18px;
    display: flex; align-items: center; justify-content: center; gap: 14px;
  }
  .brand-mark { width: 58px; height: 58px; background: var(--navy); flex: none; }
  .brand-name {
    font-family: "Lato", sans-serif; font-weight: 900; color: var(--navy);
    text-transform: uppercase; line-height: 1.05; font-size: 34px;
  }
  .brand-name span { display: block; font-size: 20px; letter-spacing: 1px; }
  .features { position: absolute; top: 300px; left: 0; width: 1200px; font-family: "Questrial", sans-serif; font-size: 34px; color: var(--ink); }
  .feature { position: absolute; display: flex; align-items: center; gap: 16px; white-space: nowrap; }
  .feature svg { width: 52px; height: 42px; }
  .feature--quality { left: 720px; top: 0; }
  .feature--delivery { left: 220px; top: 70px; }
  .feature--innovation { left: 720px; top: 64px; }
  .bhag { position: absolute; top: 432px; left: 70px; width: 1060px; text-align: center; }
  .bhag-title { display: flex; align-items: center; gap: 14px; font-weight: 900; color: var(--deep-blue); font-size: 36px; letter-spacing: 1px; }
  .bhag-title::before, .bhag-title::after { content: ""; flex: 1; height: 1px; background: var(--rule); margin-top: 10px; }
  .bhag-statement { margin-top: 8px; font-size: 22px; }
  .goals { position: absolute; top: 545px; left: 70px; width: 1060px; display: flex; gap: 30px; }
  .goal-card { flex: 1; border-radius: 10px; overflow: hidden; box-shadow: 0 8px 12px rgba(0,0,0,.3); height: 170px; background: linear-gradient(135deg, #2a56b0 0%, var(--deep-blue) 60%, #0f2f78 100%); }
  .goal-card h2 {
    background: linear-gradient(180deg, #6a6c70, var(--charcoal));
    color: #fff; text-align: center; font-size: 18px; font-weight: 700; letter-spacing: .5px;
    padding: 10px 0; border-bottom: 4px solid #d7dbe3;
  }
  .goal-card ol { list-style: none; counter-reset: goal; padding: 12px 18px; color: #fff; font-size: 14px; }
  .goal-card li { counter-increment: goal; padding: 4px 0; }
  .goal-card li::before { content: counter(goal) ". "; font-weight: 700; margin-right: 6px; }
  .goal-card--quarter li { font-size: 12.5px; }
  .footer { position: absolute; left: 0; top: 790px; width: 1200px; height: 64px; background: var(--slate); display: flex; align-items: center; justify-content: center; gap: 50px; color: #fff; font-size: 15px; font-weight: 700; }
  .footer-item { display: flex; align-items: center; gap: 10px; }
  .footer-item svg { width: 22px; height: 22px; }
  .footer-stripe { position: absolute; left: 0; top: 860px; width: 1200px; height: 10px; background: var(--brand-blue); }
  .footer-stripe--thin { top: 874px; height: 3px; background: var(--deep-blue); }
</style>
</head>
<body>
<main class="poster">
  <svg class="hero" width="1200" height="320" viewBox="0 0 1200 320">
    <defs>
      <linearGradient id="site" x1="0" y1="0" x2="1" y2="1">
        <stop offset="0" stop-color="#9a8f7e"/>
        <stop offset=".5" stop-color="#b9a789"/>
        <stop offset="1" stop-color="#7f6f5c"/>
      </linearGradient>
    </defs>
    <polygon role="img" aria-label="Photo of a construction crew and excavators working on a downtown street" points="0,0 1200,0 1200,250 1000,150 380,215 380,290 0,300" fill="url(#site)"/>
    <polyline points="380,222 1000,157 1200,257" fill="none" stroke="var(--navy)" stroke-width="6"/>
    <polyline points="380,232 1000,168 1200,268" fill="none" stroke="var(--brand-blue)" stroke-width="3"/>
    <polyline points="0,306 380,297" fill="none" stroke="var(--navy)" stroke-width="6"/>
  </svg>

  <div class="brand-panel">
    <div class="brand-mark"></div>
    <div class="brand-name">Harlow<span>Construction</span></div>
  </div>

  <section class="features">
    <div class="feature feature--quality">
      <svg viewBox="0 0 52 42"><circle cx="26" cy="21" r="12" fill="none" stroke="var(--deep-blue)" stroke-width="5" stroke-dasharray="5 3"/><circle cx="26" cy="21" r="6" fill="var(--deep-blue)"/></svg>
      Quality Construction
    </div>
    <div class="feature feature--delivery">
      <svg viewBox="0 0 52 42"><rect x="2" y="6" width="30" height="24" rx="2" fill="var(--deep-blue)"/><path d="M32 14h10l8 8v8H32z" fill="var(--deep-blue)"/><circle cx="12" cy="34" r="5" fill="#fff" stroke="var(--deep-blue)" stroke-width="3"/><circle cx="40" cy="34" r="5" fill="#fff" stroke="var(--deep-blue)" stroke-width="3"/></svg>
      First class Delivery
    </div>
    <div class="feature feature--innovation">
      <svg viewBox="0 0 52 42"><path d="M10 6l32 32" stroke="var(--deep-blue)" stroke-width="5" stroke-linecap="round"/><path d="M40 6L12 34" stroke="var(--deep-blue)" stroke-width="5" stroke-linecap="round"/><circle cx="42" cy="8" r="6" fill="none" stroke="var(--deep-blue)" stroke-width="3"/></svg>
      Innovative Solutions
    </div>
  </section>

  <section class="bhag">
    <h1 class="bhag-title">BHAG</h1>
    <p class="bhag-statement">Become one of the most admired construction companies in the markets we serve within the next 10 years</p>
  </section>

  <section class="goals">
    <article class="goal-card">
      <h2>3 – 5 YEAR GOALS</h2>
      <ol>
        <li>Generate 35m in revenue by 2020</li>
        <li>Have a 50/50 mix of Public-Private job mix</li>
        <li>Maintain 15% annual growth</li>
      </ol>
    </article>
    <article class="goal-card">
      <h2>1 YEAR GOALS</h2>
      <ol>
        <li>$24M in revenue with better margins</li>
        <li>14% gross margin on year</li>
        <li>Business development begins to pay off</li>
        <li>Continue recruiting great &amp; talented people</li>
      </ol>
    </article>
    <article class="goal-card goal-card--quarter">
      <h2>DYNAMIC QUARTER GOAL</h2>
      <ol>
        <li>Lorem Ipsum is simply dummy text.</li>
        <li>Lorem Ipsum is simply dummy text.</li>
        <li>Lorem Ipsum is simply dummy text.</li>
        <li>Lorem Ipsum is simply dummy text.</li>
      </ol>
    </article>
  </section>

  <footer class="footer">
    <div class="footer-item">
      <svg viewBox="0 0 24 24"><path d="M12 3L2 12h3v9h5v-6h4v6h5v-9h3z" fill="#fff"/></svg>
      820 Foundry Lane Riverton, Ohio 45012
    </div>
    <div class="footer-item">
      <svg viewBox="0 0 24 24"><path d="M6 3l4 4-2 3c1 2 4 5 6 6l3-2 4 4-3 3C10 21 3 14 3 6z" fill="#fff"/></svg>
      555.014.2290
    </div>
    <div class="footer-item">
      <svg viewBox="0 0 24 24" fill="none" stroke="#fff" stroke-width="2"><circle cx="12" cy="12" r="9"/><path d="M3 12h18M12 3c3 3 3 15 0 18M12 3c-3 3-3 15 0 18"/></svg>
      www.harlowconstruction.com
    </div>
  </footer>
  <div class="footer-stripe"></div>
  <div class="footer-stripe footer-stripe--thin"></div>
</main>
</body>
</html>
```